第3期を迎えるSDGs啓蒙活動である『ハナ凧プロジェクト』のポスターデザインを募集します。
第3期は50社超が参加します。

【作成条件】
・ポスターには参加企業のロゴマークを記載(各社データあり)
・イラスト、写真は問いません
・環境に特化する必要はありません

第2期のポスターデザインを参考にアップしておきますが、卵にはこだわらないで下さい。

今回は参加企業に様々な業種があり、特に金融機関各店舗に掲示するので、高齢の方にも分かりやすいものを選定させて戴きました。
まだまだSDGsの認知も浸透していないので、とにかく分かりやすいという事での選定となりました。

今回は素敵なポスターのご提案に心より感謝申し上げます。
今後も定期的なSDGs勉強会を全国で開催していくので、チラシデザインなどを定期的に発注予定です。
ご縁がございましたら是非ともご提案をお待ちしております。
ありがとうございました。

```html
<!DOCTYPE html>
<html lang="ja">
<head>
<meta charset="utf-8">
<title>未来を考えるハナ凧プロジェクト2021</title>
<link rel="stylesheet" href="https://fonts.googleapis.com/css2?family=Noto+Sans+JP:wght@400;700;900&family=Noto+Serif+JP:wght@500;700&family=Montserrat:wght@900&display=swap">
<style>
  :root {
    --brand-blue: #1f9ad8;
    --navy: #1c3f8f;
    --ink: #333;
    --muted: #666;
    --rule: #b9c6d3;
    --paper: #ffffff;
    --globe-light: #8ccbee;
    --globe-mid: #3f8fc6;
    --globe-deep: #235f93;
    --c1: #e5332a; --c2: #f39800; --c3: #f5c400; --c4: #8fc31f;
    --c5: #009944; --c6: #00a0c6; --c7: #0068b7; --c8: #920783; --c9: #e4007f;
  }
  html, body { margin: 0; padding: 0; overflow: hidden; background: var(--paper); }
  .poster {
    position: relative; width: 848px; height: 1200px; overflow: hidden;
    background: var(--paper); font-family: "Noto Sans JP", sans-serif; color: var(--ink);
  }
  .title-band {
    position: absolute; left: 22px; right: 22px; top: 16px; height: 62px;
    background: var(--brand-blue); border-radius: 0 0 14px 14px;
    display: flex; align-items: center; justify-content: center;
    color: #fff; font-weight: 900; font-size: 32px; letter-spacing: 2px;
  }
  .hero-art {
    position: absolute; left: 144px; top: 120px; width: 560px; height: 560px;
    border-radius: 50%;
    background: radial-gradient(circle at 45% 42%, var(--globe-light) 0%, var(--globe-mid) 50%, var(--globe-deep) 78%, rgba(35,95,147,0) 100%);
  }
  .slogan {
    position: absolute; left: 0; right: 0; top: 408px; display: flex; justify-content: center; gap: 72px;
    font-family: "Montserrat", sans-serif; font-weight: 900; font-size: 48px; letter-spacing: 0;
  }
  .slogan span:nth-child(9n+1){color:var(--c1)} .slogan span:nth-child(9n+2){color:var(--c2)}
  .slogan span:nth-child(9n+3){color:var(--c3)} .slogan span:nth-child(9n+4){color:var(--c4)}
  .slogan span:nth-child(9n+5){color:var(--c5)} .slogan span:nth-child(9n+6){color:var(--c6)}
  .slogan span:nth-child(9n+7){color:var(--c7)} .slogan span:nth-child(9n+8){color:var(--c8)}
  .slogan span:nth-child(9n+9){color:var(--c9)}
  .headline {
    position: absolute; left: 0; right: 0; top: 712px; margin: 0; text-align: center;
    font-family: "Noto Serif JP", serif; font-weight: 700; font-size: 50px; line-height: 1.2;
    color: var(--navy); letter-spacing: 4px;
  }
  .lead {
    position: absolute; left: 0; right: 0; top: 800px; margin: 0; text-align: center;
    font-family: "Noto Serif JP", serif; font-weight: 500; font-size: 15px; line-height: 1.6; color: var(--navy);
  }
  .goals-row { position: absolute; left: 36px; top: 888px; display: flex; align-items: center; gap: 14px; }
  .goals-name { font-weight: 900; font-size: 20px; color: var(--brand-blue); }
  .goals-note { font-size: 10px; color: var(--muted); }
  .rule { position: absolute; left: 36px; right: 36px; top: 928px; border-top: 1px solid var(--rule); }
  .hosts {
    position: absolute; left: 36px; right: 36px; top: 938px;
    display: flex; gap: 24px; align-items: center;
    font-size: 13px; font-weight: 700; color: var(--navy);
  }
  .label { font-size: 10px; font-weight: 400; color: var(--muted); }
  .sponsors {
    position: absolute; left: 36px; right: 36px; top: 972px;
    display: grid; grid-template-columns: repeat(6, 1fr); row-gap: 6px; column-gap: 10px;
    font-size: 11px; line-height: 16px; font-weight: 700; color: var(--ink);
  }
  .sponsors span { white-space: nowrap; }
  .sponsors span:nth-child(3n) { color: var(--navy); }
  .sponsors span:nth-child(4n+1) { color: var(--c5); }
</style>
</head>
<body>
<div class="poster">
  <header class="title-band">未来を考えるハナ凧プロジェクト2021</header>

  <div class="hero-art" role="img" aria-label="地球の上に砂時計が置かれ、上部の氷の上にシロクマが立っているイラスト"></div>

  <div class="slogan">
    <div><span>L</span><span>E</span><span>T</span><span>'</span><span>S</span> <span>S</span><span>A</span><span>V</span><span>E</span></div>
    <div><span>O</span><span>U</span><span>R</span> <span>P</span><span>L</span><span>A</span><span>N</span><span>E</span><span>T</span></div>
  </div>

  <h1 class="headline">もう時間がありません</h1>
  <p class="lead">
    地球温暖化問題は先送りに出来ない所まで来ています。<br>
    御社素材のリサイクル・リユース、プラスチック削減、紙からのデジタル化等、<br>
    プロジェクト賛同企業一丸となって環境問題に取組んでいます。
  </p>

  <div class="goals-row">
    <span class="goals-name">みらい目標アクション</span>
    <span class="goals-note">私たちは持続可能な社会の実現を応援しています。</span>
  </div>
  <div class="rule"></div>

  <div class="hosts">
    <span class="label">主催</span><span>あおば銀行</span><span>みなと信用金庫</span><span>ひかり証券</span><span>そよ風保険</span><span>さくら通信</span>
  </div>

  <div class="sponsors">
    <span>北星印刷</span><span>みどり建設</span><span>あさひ物産</span><span>つばさ運輸</span><span>こだま電機</span><span>はるか食品</span>
    <span>青葉商事</span><span>なぎさ工業</span><span>いずみ製紙</span><span>かえで不動産</span><span>ほたる薬局</span><span>みずほ野菜</span>
    <span>とうげ木材</span><span>しらさぎ交通</span><span>ふたば化学</span><span>やまびこ設備</span><span>あかね衣料</span><span>ゆうひ電設</span>
    <span>こはく精工</span><span>わかば保育</span><span>すずらん産業</span><span>たちばな機械</span><span>ひばり通商</span><span>かすみ物流</span>
    <span>みさき水産</span><span>つむぎ繊維</span><span>あおい技研</span><span>さざなみ塗装</span><span>はやて自動車</span><span>もみじ製菓</span>
    <span>いろは広告</span><span>ときわ鋼材</span><span>うらら家具</span><span>ひなた住宅</span><span>こもれび園芸</span><span>そらいろ電工</span>
    <span>きらら硝子</span><span>ゆずりは会計</span><span>あけぼの酒造</span><span>なのはな農園</span><span>しずく水道</span><span>ほのか美容</span>
    <span>くすのき医療</span><span>たんぽぽ介護</span><span>みやび呉服</span><span>はまなす観光</span><span>かがやき照明</span><span>つくし文具</span>
    <span>せせらぎ環境</span><span>おおぞら航空</span><span>ふじなみ建材</span><span>ひいらぎ警備</span><span>いちょう金属</span><span>あじさい情報</span>
  </div>
</div>
</body>
</html>
```